label design for oral care product

Kindly invite you to design bottle label (114 mm*40 mm) for our product, a kind of oral care product. The GEL is different from our previous cleanser product, as the pic we uploaded for demonstration. The color of frosted glass bottle is dark green, but the cap is white. You could download the pic of bottle among the uploaded files. The logo file and label content description are attached too. Please check them. Our product is made from many kinds of natural plant extracts, which includes herb and fruit. I wish the label would make our product look high-end and reliable. And it would be better if you could give some advice on paper material and special requirements for printing, related to your design. I value the texture of label too, because I think that stands for the quality of products. No color limitation for the use of our logo.
Target Market(s)
20-40 female, who value oral health.
Colors
Designer to choose colors to be used in the design.
Look and feel
Each slider illustrates characteristics of the customer's brand and the style your logo design should communicate.

```html
<!DOCTYPE html>
<html lang="en">
<head>
<meta charset="utf-8">
<title>Cleara Gel – Bottle Label</title>
<link href="https://fonts.googleapis.com/css2?family=Jost:wght@300;400;600&family=Roboto+Condensed:wght@300;400;700&display=swap" rel="stylesheet">
<style>
  :root {
    --page-bg: #eceae4;
    --olive: #4a4d22;
    --olive-deep: #2d2e12;
    --olive-front: #2b2c11;
    --ink-light: #e6e3cf;
    --gold-dark: #b07a10;
    --gold-mid: #e6b93c;
    --gold-light: #fbe08a;
    --stone: #8c8a78;
  }
  * { box-sizing: border-box; margin: 0; padding: 0; }
  html, body { width: 1200px; height: 1200px; overflow: hidden; }
  body {
    background: var(--page-bg);
    display: flex; align-items: center; justify-content: center;
    font-family: "Roboto Condensed", "Arial Narrow", sans-serif;
  }
  .label {
    width: 1140px; height: 400px;
    display: flex;
    border-radius: 10px; overflow: hidden;
    box-shadow: 0 10px 30px rgba(0,0,0,.18);
  }
  .panel { position: relative; width: 380px; height: 400px; }
  .panel--side {
    background: linear-gradient(90deg, var(--olive-deep) 0%, var(--olive) 55%, var(--olive-deep) 100%);
    color: var(--ink-light);
    font-weight: 300;
    font-size: 14px; line-height: 1.32;
  }
  .panel--front { background: var(--olive-front); }
  .panel svg.shapes { position: absolute; inset: 0; }
  .copy { position: absolute; left: 34px; right: 28px; top: 40px; }
  .copy p + p { margin-top: 14px; }
  .copy strong { font-weight: 700; }
  .copy--right { left: 30px; right: 34px; top: 40px; }
  .made-in { position: absolute; left: 30px; top: 300px; color: var(--ink-light); font-size: 14px; font-weight: 300; }

  .brand {
    position: absolute; right: 30px; top: 52px;
    display: flex; align-items: center; gap: 8px;
    font-family: "Jost", sans-serif; font-weight: 600;
    font-size: 34px; line-height: 1; color: var(--gold-mid);
    letter-spacing: -0.5px;
  }
  .brand .dot { width: 12px; height: 12px; border-radius: 50%; background: var(--gold-mid); }

  .product-type {
    position: absolute; left: 22px; top: 384px;
    width: 270px;
    transform: rotate(-90deg); transform-origin: top left;
    font-family: "Jost", sans-serif; color: var(--olive-front);
    line-height: 1;
  }
  .product-name { font-size: 40px; font-weight: 600; letter-spacing: 0.5px; }
  .product-name span { font-weight: 300; }
  .product-claim { font-size: 19px; font-weight: 300; line-height: 1.02; margin-top: 4px; }
  .product-tagline { font-family: "Roboto Condensed", sans-serif; font-size: 10.5px; font-weight: 400; line-height: 1.1; margin-top: 8px; }
  .product-volume { font-size: 15px; font-weight: 400; margin-top: 12px; }
</style>
</head>
<body>
  <div class="label">
    <section class="panel panel--side panel--left">
      <svg class="shapes" width="380" height="400" viewBox="0 0 380 400">
        <defs>
          <linearGradient id="goldLeft" x1="0" y1="0" x2="1" y2="1">
            <stop offset="0" stop-color="#d9a42a"/><stop offset="0.6" stop-color="#f6d269"/><stop offset="1" stop-color="#fbe08a"/>
          </linearGradient>
        </defs>
        <polygon points="12,250 12,392 128,392" fill="url(#goldLeft)"/>
      </svg>
      <div class="copy">
        <p>Lorem ipsum dolor sit amet, consectetur adipiscing elit Proin non risus sollicitudin leo luctus placerat. Nulla eu tellus at leo blandit rutrum. Pellentesque sodales leo sed dui placerat, venenatis tincidunt metus lacinia. Maecenas auctor odio facilisis turpis vehicula eleifend. Sed aliquet tellus eu hendrerit mollis.</p>
        <p><strong>Directions:</strong> Drop on the teeth directly after brushing. Or, put into clear aligners before wearing again. No need to rinse your mouth with water.</p>
      </div>
    </section>

    <section class="panel panel--front">
      <svg class="shapes" width="380" height="400" viewBox="0 0 380 400">
        <defs>
          <linearGradient id="goldFront" x1="0" y1="0" x2="1" y2="0.4">
            <stop offset="0" stop-color="#c99320"/><stop offset="0.35" stop-color="#fbe08a"/><stop offset="0.7" stop-color="#e8b63a"/><stop offset="1" stop-color="#b07a10"/>
          </linearGradient>
        </defs>
        <polygon points="14,18 14,392 270,392" fill="url(#goldFront)"/>
        <polygon points="212,232 212,362 296,358" fill="var(--stone)"/>
      </svg>
      <div class="brand">Lumo Mint<span class="dot"></span></div>
      <div class="product-type">
        <div class="product-name">CLEARA<span>GEL</span></div>
        <div class="product-claim">DAILY DEFENCE<br>FOR GUM COMFORT</div>
        <div class="product-tagline">a Gentle Way to Keep Teeth<br>Fresh and Gums Resilient</div>
        <div class="product-volume">30 ml / 1 fl oz</div>
      </div>
    </section>

    <section class="panel panel--side panel--right">
      <svg class="shapes" width="380" height="400" viewBox="0 0 380 400">
        <defs>
          <linearGradient id="goldRight" x1="1" y1="0" x2="0" y2="1">
            <stop offset="0" stop-color="#d9a42a"/><stop offset="0.6" stop-color="#f6d269"/><stop offset="1" stop-color="#fbe08a"/>
          </linearGradient>
        </defs>
        <polygon points="368,250 368,392 252,392" fill="url(#goldRight)"/>
      </svg>
      <div class="copy copy--right">
        <p>Maecenas ultricies felis vitae eros pellentesque. Nunc id ante eget metus fermentum dictum et. Proin id velit gravida, dictum ante eget, gravida. Proin lacinia sem nec est sodales, nec. Proin congue arcu eu pharetra facilisis. Nulla aliquet diam porttitor scelerisque varius. Maecenas sed urna quis tortor lobortis.</p>
        <p style="margin-top:46px"><strong>Contains:</strong> a proprietary blend of natural plant extract including Angelica, Radix Rehmanniae, Coptis, Honeysuckle, Echinacea, Sage, Chamomile, Acerola cherry.</p>
      </div>
      <div class="made-in">Made in Taiwan</div>
    </section>
  </div>
</body>
</html>
```